Home Inspection Postcard Design

Home inspection. Attached is my old postcard. I would like the card to have the same verbage on it - front and back. but I would like the house graphic and the colors to be blues. The only changes to the information is the website address is www.brambleridgehi.com. THe PO Box is now 718 rather than 369, and I wanted to add my email address which is brambleridgehi@mailvexo.net. I would like to keep the $25 off box but add "or a 10% military discount, which ever is greater" or something like that .If you could mock something up for me I would really appreciate it. I would also like a glossy finish on the cards

```html
<!DOCTYPE html>
<html lang="en">
<head>
<meta charset="utf-8">
<title>Bramble Ridge Home Inspection Postcard</title>
<link href="https://fonts.googleapis.com/css2?family=Oswald:wght@500;700&family=Open+Sans:wght@400;600;700&display=swap" rel="stylesheet">
<style>
  :root{
    --page:#e9e6e1;
    --paper:#ffffff;
    --navy:#13406e;
    --navy-dark:#0b2a4c;
    --sky:#2f8fd6;
    --ice:#8fd0ff;
    --ink:#1d1d1d;
    --bar:#0a1f38;
    --photo-a:#c3d6e6;
    --photo-b:#7f9fbd;
    --offer-a:#e3f3ff;
    --offer-b:#9ccff3;
    --line:#b8b8b8;
  }
  *{box-sizing:border-box;margin:0;padding:0}
  html,body{width:800px;height:1200px;overflow:hidden;background:var(--page);font-family:"Open Sans",Arial,sans-serif;color:var(--ink)}
  .card{position:absolute;left:40px;width:720px;height:510px;background:var(--paper);overflow:hidden;box-shadow:0 6px 18px rgba(0,0,0,.25)}
  .card--front{top:40px}
  .card--back{top:630px}
  .card svg.shapes{position:absolute;inset:0}
  .abs{position:absolute}

  /* front */
  .brand{left:26px;top:22px;display:flex;align-items:center;gap:10px}
  .brand__mark{width:34px;height:34px;background:var(--navy)}
  .brand__name{font-family:"Oswald",sans-serif;font-weight:700;font-size:22px;color:var(--navy);line-height:1}
  .brand__sub{font-size:8px;color:var(--ink);margin-top:3px}
  .headline{left:26px;top:110px;font-family:"Oswald",sans-serif;font-weight:700;line-height:1}
  .headline__top{font-size:32px;color:var(--sky)}
  .headline__bottom{font-size:60px;color:var(--ink);margin-top:2px}
  .tagline{left:26px;top:234px;font-family:"Oswald",sans-serif;font-weight:500;font-size:15px;color:var(--ice);letter-spacing:.5px}
  .front-copy{left:26px;top:274px;width:420px;color:#fff;font-size:10.6px;line-height:1.45}
  .front-copy p+p{margin-top:10px}
  .offer{left:478px;top:268px;width:214px;height:118px;border-radius:10px;background:linear-gradient(180deg,var(--offer-a),var(--offer-b));text-align:center;padding-top:14px;color:var(--navy)}
  .offer__big{font-family:"Oswald",sans-serif;font-weight:700;font-size:34px;line-height:1}
  .offer__small{font-size:11px;font-weight:600;color:var(--ink)}
  .offer__alt{font-family:"Oswald",sans-serif;font-weight:500;font-size:16px;margin-top:6px}
  .contact-bar{left:0;top:470px;width:720px;height:40px;display:flex;justify-content:space-between;align-items:center;padding:0 26px;color:#fff;font-size:12.5px;font-weight:600}
  .contact-bar strong{font-size:15px}
  .contact-bar .web{display:flex;align-items:center;gap:7px}
  .dot{width:9px;height:9px;border-radius:50%;background:var(--ice);flex:none}

  /* back */
  .back-title{left:26px;top:28px;font-family:"Oswald",sans-serif;font-weight:700;font-size:20px;color:var(--ice)}
  .back-copy{left:26px;top:68px;width:268px;color:#fff;font-size:10.4px;line-height:1.45}
  .back-copy p+p{margin-top:10px}
  .back-contact{left:26px;top:412px;color:#fff;font-size:11.5px;font-weight:600;line-height:1.8}
  .back-contact li{list-style:none;display:flex;align-items:center;gap:8px}
  .stamp{left:620px;top:22px;width:72px;height:84px;border:1.5px solid var(--line)}
  .address-lines{left:420px;top:280px;width:270px}
  .address-lines span{display:block;height:34px;border-bottom:1.5px solid var(--line)}
</style>
</head>
<body>

<section class="card card--front">
  <svg class="shapes" width="720" height="510" viewBox="0 0 720 510">
    <defs>
      <linearGradient id="photo" x1="0" y1="0" x2="1" y2="1">
        <stop offset="0" stop-color="var(--photo-a)"/>
        <stop offset="1" stop-color="var(--photo-b)"/>
      </linearGradient>
    </defs>
    <path d="M340,0 H720 V300 H440 C395,230 360,120 340,0 Z" fill="url(#photo)" role="img" aria-label="Photo of a two-storey family house seen through an inspector's magnifying glass"/>
    <path d="M322,0 H340 C360,120 395,230 440,300 H418 C376,232 342,120 322,0 Z" fill="var(--sky)"/>
    <rect x="0" y="226" width="450" height="32" fill="var(--navy-dark)"/>
    <rect x="0" y="258" width="720" height="212" fill="var(--navy)"/>
    <rect x="0" y="470" width="720" height="40" fill="var(--bar)"/>
  </svg>

  <div class="abs brand">
    <span class="brand__mark"></span>
    <div>
      <div class="brand__name">Bramble Ridge</div>
      <div class="brand__sub">Home Inspection Services LLC</div>
    </div>
  </div>

  <h1 class="abs headline">
    <div class="headline__top">WE LEAVE NO STONE</div>
    <div class="headline__bottom">UNTURNED</div>
  </h1>

  <div class="abs tagline">CONFIDENCE IN HOME BUYING</div>

  <div class="abs front-copy">
    <p>Enjoy the comfort of peace-of-mind before buying your new home. Our trained professionals inspect the property and immediately present you with a detailed, yet clear report. They will answer any questions you may have.</p>
    <p>Join our experienced inspectors in their tour of the property. They will acquaint you with its strengths and weaknesses. You will feel confident in their judgement and thoroughness. Many Realtors, sellers, home buyers, mortgage companies and relocation companies have used our comprehensive report and services to their satisfaction.</p>
  </div>

  <div class="abs offer">
    <div class="offer__big">25% off</div>
    <div class="offer__small">services with postcard</div>
    <div class="offer__alt">or 10% military discount</div>
  </div>

  <div class="abs contact-bar">
    <span><strong>Call 912-555-0147</strong> to schedule your appointment</span>
    <span class="web"><span class="dot"></span>www.brambleridgehi.com</span>
  </div>
</section>

<section class="card card--back">
  <svg class="shapes" width="720" height="510" viewBox="0 0 720 510">
    <path d="M0,0 H330 C300,170 300,340 330,510 H0 Z" fill="var(--navy)"/>
    <path d="M330,0 H344 C314,170 314,340 344,510 H330 C300,340 300,170 330,0 Z" fill="var(--sky)"/>
    <path d="M0,0 H330 C327,20 324,40 322,60 H0 Z" fill="var(--navy-dark)"/>
  </svg>

  <h2 class="abs back-title">Why do I need an Inspection?</h2>

  <div class="abs back-copy">
    <p>The purchase of a home or commercial building is one of the largest single investments you will ever make. You should know what to expect – in terms of needed and possible repairs and maintenance. A fresh coat of paint could be hiding serious problems.</p>
    <p>Stains on the ceiling may indicate a chronic roof leak or may be simply the result of a single incident. The inspector reviews these and other clues, then presents a professional opinion as to the condition of the property to help you avoid unpleasant surprises afterward. Of course, an inspection may also point out the positive aspects of a building, as well as the type of maintenance needed to keep it in proper shape. After the inspection, you will have a much clearer understanding of the property, and be able to make your purchasing decision confidently.</p>
  </div>

  <ul class="abs back-contact">
    <li><span class="dot"></span>912-555-0147</li>
    <li><span class="dot"></span>brambleridgehi@mailvexo.net</li>
    <li><span class="dot"></span>www.brambleridgehi.com</li>
  </ul>

  <div class="abs stamp"></div>
  <div class="abs address-lines"><span></span><span></span><span></span><span></span></div>
</section>

</body>
</html>
```